Melissa Dorvan Personal Business Card

I like orange. It's would better if my card have an orange background
Address: 5820 Halvers Lane #417
San Jose
California
US
Tel: 4085172049

Industry/Entity Type

Business

```html
<!DOCTYPE html>
<html lang="en">
<head>
<meta charset="utf-8">
<title>Melissa Dorvan – Business Card</title>
<link rel="stylesheet" href="https://fonts.googleapis.com/css2?family=Playfair+Display:wght@700;900&family=Tenor+Sans&display=swap">
<style>
  :root {
    --canvas: #ffffff;
    --card-edge: #3a3a3a;
    --orange: #f47920;
    --halftone: #e4542f;
    --crimson: #b01117;
    --ink: #111111;
    --name: #ffffff;
  }
  html, body {
    margin: 0;
    padding: 0;
    width: 1200px;
    height: 1000px;
    overflow: hidden;
    background: var(--canvas);
  }
  .canvas {
    position: relative;
    width: 1200px;
    height: 1000px;
  }
  .card {
    position: absolute;
    left: 206px;
    top: 261px;
    width: 783px;
    height: 475px;
    border: 1px solid var(--card-edge);
    background: #fff;
    box-sizing: border-box;
  }
  .card-field {
    position: absolute;
    left: 224px;
    top: 279px;
    width: 750px;
    height: 441px;
    background: var(--orange);
    overflow: hidden;
  }
  .halftone-band {
    position: absolute;
    left: 60px;
    top: 0;
    width: 630px;
    height: 258px;
  }
  .name-block {
    position: absolute;
    left: 466px;
    top: 261px;
    width: 266px;
    height: 266px;
    background: var(--crimson);
    display: flex;
    align-items: center;
    justify-content: center;
  }
  .name {
    margin: 0;
    padding-top: 8px;
    font-family: "Playfair Display", "Bodoni Moda", serif;
    font-weight: 900;
    font-size: 40px;
    line-height: 50px;
    letter-spacing: 0.5px;
    color: var(--name);
    text-align: center;
    text-transform: uppercase;
  }
  .contact {
    position: absolute;
    left: 224px;
    width: 750px;
    text-align: center;
    font-family: "Tenor Sans", "Optima", sans-serif;
    font-size: 22px;
    color: var(--ink);
    margin: 0;
  }
  .contact-address { top: 592px; }
  .contact-phone { top: 665px; letter-spacing: 0.5px; }
  .icon {
    position: absolute;
    display: block;
  }
  .icon-pin { left: 587px; top: 559px; }
  .icon-phone { left: 584px; top: 631px; }
</style>
</head>
<body>
<div class="canvas">
  <div class="card"></div>
  <div class="card-field">
    <svg class="halftone-band" role="img" aria-label="Halftone dot pattern in red-orange fading toward the edges" viewBox="0 0 630 258" width="630" height="258">
      <defs>
        <linearGradient id="halftone-fade-x" x1="0" y1="0" x2="1" y2="0">
          <stop offset="0" stop-color="var(--halftone)" stop-opacity="0.1"/>
          <stop offset="0.35" stop-color="var(--halftone)" stop-opacity="0.85"/>
          <stop offset="0.65" stop-color="var(--halftone)" stop-opacity="0.85"/>
          <stop offset="1" stop-color="var(--halftone)" stop-opacity="0.1"/>
        </linearGradient>
      </defs>
      <rect x="0" y="0" width="630" height="258" fill="url(#halftone-fade-x)"/>
    </svg>
  </div>
  <div class="name-block">
    <h1 class="name">Melissa<br>Dorvan</h1>
  </div>

  <svg class="icon icon-pin" width="22" height="30" viewBox="0 0 22 30" aria-hidden="true">
    <path d="M11 0C4.9 0 0 4.9 0 11c0 7.5 11 19 11 19s11-11.5 11-19C22 4.9 17.1 0 11 0z" fill="var(--crimson)"/>
    <circle cx="11" cy="11" r="3.6" fill="var(--orange)"/>
  </svg>
  <p class="contact contact-address">5820 Halvers Lane #417, San Jose, California, US</p>

  <svg class="icon icon-phone" width="28" height="28" viewBox="0 0 28 28" aria-hidden="true">
    <circle cx="14" cy="14" r="14" fill="var(--crimson)"/>
    <rect x="9" y="6" width="10" height="16" rx="1.8" fill="none" stroke="var(--orange)" stroke-width="1.8"/>
    <line x1="12" y1="19" x2="16" y2="19" stroke="var(--orange)" stroke-width="1.4"/>
  </svg>
  <p class="contact contact-phone">4085172049</p>
</div>
</body>
</html>
```